Award-winnning Estate Agent needs a premium version of their 'For Sale' board design

We need a premium option for our 'For Sale' board design. We have a standard board that is attached to this brief, but were are looking to have a premium design version that we will use when selling exclusive properties. Our company name is Harbour Lane Estates and the name for this is exclusive selection is: 'The Harbour Collection'. The design needs to work with our current brand, but have a distinctive PREMIUM feel to it. I have uploaded the barnd guidelines and also some of the exisisting logo variations. We do NOT need a new logo but feel free to play around with colours, fonts, sizes etc. for the sign.

Target Market(s)

Property buyers & house hunters

Industry/Entity Type

Real Estate - Residential Property

Font styles to use
Sans Serif

Requirements
Must have
• A premium fee, must be square design, must be easy to read when driving past the sign
Nice to have
• I'm open ot ideas

```html
<!DOCTYPE html>
<html lang="en">
<head>
<meta charset="utf-8">
<title>Harbour Lane Estates – The Harbour Collection board options</title>
<link rel="stylesheet" href="https://fonts.googleapis.com/css2?family=Bebas+Neue&family=Montserrat:wght@500;600;700;800&family=Open+Sans:wght@700&display=swap">
<style>
  :root{
    --purple:#402b6e;
    --purple-deep:#3b2868;
    --blue:#4670a8;
    --sky:#5aa3d1;
    --white:#ffffff;
    --grey-dark:#8e8e8e;
    --grey-light:#c1c1c1;
    --ink:#000000;
  }
  *{margin:0;padding:0;box-sizing:border-box}
  html,body{width:1200px;height:3416px;overflow:hidden}
  body{background:var(--white);font-family:"Montserrat",sans-serif;position:relative}

  .option{position:absolute;left:0;width:1200px}
  .option--one{top:0;height:1140px;background:var(--grey-dark)}
  .option--two{top:1140px;height:1135px;background:var(--white)}
  .option--three{top:2275px;height:1141px;background:var(--grey-light)}

  .option-label{
    position:absolute;left:72px;
    transform:rotate(-90deg);transform-origin:left top;
    font:600 29px "Montserrat",sans-serif;letter-spacing:.5px;
    color:var(--white);white-space:nowrap;
  }
  .option--one .option-label{top:305px}
  .option--two .option-label{top:298px;color:var(--ink)}
  .option--three .option-label{top:305px}

  .board{
    position:absolute;left:207px;width:822px;height:822px;
    box-shadow:18px 22px 30px rgba(0,0,0,.28);
    overflow:hidden;
  }
  .option--one .board{top:159px}
  .option--two .board{top:154px}
  .option--three .board{top:161px}

  .collection-title{
    text-align:center;color:var(--white);white-space:nowrap;
    font-family:"Montserrat",sans-serif;font-weight:600;
  }
  .sale-headline{
    text-align:center;color:var(--white);white-space:nowrap;line-height:1;
  }
  .sale-headline--condensed{
    font-family:"Bebas Neue",sans-serif;font-size:252px;letter-spacing:4px;
    text-shadow:6px 6px 8px rgba(0,0,0,.25);
  }
  .brand{
    display:flex;align-items:center;justify-content:center;gap:22px;
  }
  .brand-square{width:66px;height:66px;background:var(--sky);flex:none}
  .brand-name{font:600 56px "Montserrat",sans-serif;color:var(--purple);white-space:nowrap}
  .phone{font-family:"Montserrat",sans-serif;font-weight:700;text-align:center;white-space:nowrap;letter-spacing:-1px}
  .web{font:700 39px "Open Sans",sans-serif;color:var(--purple);text-align:center;white-space:nowrap}

  /* Option one */
  .option--one .board{background:linear-gradient(100deg,var(--purple-deep) 0%,var(--blue) 100%)}
  .option--one .collection-title{position:absolute;top:28px;left:0;width:100%;font-size:50px;letter-spacing:1px}
  .option--one .sale-headline{position:absolute;top:74px;left:0;width:100%}
  .option--one .panel{
    position:absolute;left:14px;top:312px;width:793px;height:494px;background:var(--white);
  }
  .option--one .brand{position:absolute;top:190px;left:0;width:100%}
  .option--one .rule{position:absolute;left:44px;width:705px;height:2px;background:var(--purple)}
  .option--one .rule--top{top:295px}
  .option--one .rule--bottom{top:411px}
  .option--one .phone{position:absolute;top:303px;left:0;width:100%;height:106px;line-height:106px;font-size:100px;color:var(--blue)}
  .option--one .web{position:absolute;top:424px;left:0;width:100%}

  /* Option two */
  .option--two .board{background:var(--purple);border:15px solid var(--purple)}
  .option--two .top-panel{position:absolute;left:0;top:0;width:792px;height:360px;background:var(--white)}
  .option--two .brand{position:absolute;top:200px;left:0;width:100%}
  .option--two .sale-band{position:absolute;left:0;top:360px;width:792px;height:222px;background:var(--sky)}
  .option--two .collection-title{position:absolute;top:14px;left:0;width:100%;font-size:40px}
  .option--two .sale-headline{
    position:absolute;top:62px;left:0;width:100%;
    font:800 136px "Montserrat",sans-serif;letter-spacing:-3px;
    text-shadow:5px 5px 0 var(--blue);
  }
  .option--two .phone{position:absolute;top:596px;left:0;width:100%;line-height:106px;font-size:104px;color:var(--white);text-shadow:4px 4px 6px rgba(0,0,0,.3)}
  .option--two .web-band{position:absolute;left:0;top:718px;width:792px;height:74px;background:var(--white);display:flex;align-items:center;justify-content:center}

  /* Option three */
  .option--three .board{background:var(--sky);border:15px solid var(--sky)}
  .option--three .top-panel{position:absolute;left:0;top:0;width:792px;height:270px;background:var(--white)}
  .option--three .brand{position:absolute;top:160px;left:0;width:100%}
  .option--three .sale-band{position:absolute;left:0;top:270px;width:792px;height:294px;background:var(--purple)}
  .option--three .collection-title{position:absolute;top:22px;left:0;width:100%;font-size:46px;letter-spacing:3px}
  .option--three .sale-headline{position:absolute;top:62px;left:0;width:100%;font-size:236px}
  .option--three .phone{position:absolute;top:582px;left:0;width:100%;line-height:104px;font-size:100px;color:var(--white)}
  .option--three .web-band{position:absolute;left:0;top:710px;width:792px;height:82px;background:var(--white);display:flex;align-items:center;justify-content:center}
</style>
</head>
<body>

<section class="option option--one">
  <p class="option-label">Sample 1</p>
  <div class="board">
    <p class="collection-title">THE HARBOUR COLLECTION</p>
    <p class="sale-headline sale-headline--condensed">FOR SALE</p>
    <div class="panel">
      <div class="brand"><span class="brand-square"></span><span class="brand-name">Harbour Lane Estates</span></div>
      <div class="rule rule--top"></div>
      <p class="phone">01632 960214</p>
      <div class="rule rule--bottom"></div>
      <p class="web">www.harbourlaneestates.co.uk</p>
    </div>
  </div>
</section>

<section class="option option--two">
  <p class="option-label">Sample 2</p>
  <div class="board">
    <div class="top-panel">
      <div class="brand"><span class="brand-square"></span><span class="brand-name">Harbour Lane Estates</span></div>
    </div>
    <div class="sale-band">
      <p class="collection-title">THE HARBOUR COLLECTION</p>
      <p class="sale-headline">FOR SALE</p>
    </div>
    <p class="phone">01632 960214</p>
    <div class="web-band"><p class="web">www.harbourlaneestates.co.uk</p></div>
  </div>
</section>

<section class="option option--three">
  <p class="option-label">Sample 3</p>
  <div class="board">
    <div class="top-panel">
      <div class="brand"><span class="brand-square"></span><span class="brand-name">Harbour Lane Estates</span></div>
    </div>
    <div class="sale-band">
      <p class="collection-title">THE HARBOUR COLLECTION</p>
      <p class="sale-headline sale-headline--condensed">FOR SALE</p>
    </div>
    <p class="phone">01632 960214</p>
    <div class="web-band"><p class="web">www.harbourlaneestates.co.uk</p></div>
  </div>
</section>

</body>
</html>
```